Dietary supplement, Clean and simple.

Hi,
I’d like to talk about the project,

About us:
We are a dietary supplement (Vitamins, Minerals, amino acids etc.) company.
The goal is to have about 25 products at the end of this year. However, for this goal to be achieved we need a good label design to make our products represent our company values.
I’ll be here every day supporting your questions, we are fully committed to making the highest/best quality/customer experience possible.

About the design and our values:
- Professional (We are in the industry of professionalism and expertise. I would love to show we are competent at this, Id. Like to have the labels looks like we have done our research.)
- Efficient (White spacing, good use of the space available.)
- Simple (Straight forward, in 5 seconds they have to know what the product they have is/how functions. We’re trying to simplify it for the consumer.
- No distractions (the only visually “distracting” factor can be the vector art.)

The guidelines:
The goal is to have a universal design, with one element that changes (Vector art). I’ll attach a file/multiple files I think can show some visuals on what I’m looking for, and what parts of the design I think are good/bad.

Label size: 69x155mm (Front is 77.5mm)

Design whatever you think fits our image. You’re the design expert, all I care about is that it fits our company standards/image.

Use this color/font.
Font: Sans Serif
Main company color is Mind green #237D62 (Use this color for something in the design.)

What I thought would be cool/might looks ugly, who knows:
1. The front of the label: Should have 1 vector art, preferably in the top right corner. (That looks good in multiple colors. The vector can have multiple areas to color, I would prefer 2 main colors in the vector art. The interchangeable colors are used for multiple kinds of products.)
2. Text/product information on the left. The text that will have to be displayed:
- Product name for instance “Magnesium + B6”
- Description for the product for instance “Magnesium with ginger taste”
- Company name or logo. (Add ® behind it. We are soon to be trademark registered.)
3. We need to show the "daily intake" amount on the front and also the amount in the complete bottle. For instance, “Daily intake 1 capsule, 60 capsules”.
• You don’t have to design the backside of the label. After I chose a design, I’d like to chat and give specific information on what areas need to be assigned where. (Too complex because of the law.)
Updates

Hi, Please make the deadline 31 days total. I want designers to have the time to design. And not be rushed to finish it.

I want to extend the deadline because i feel like a slightly more medical look would be interesting. Hope you can come up with something!!

Target Market(s)

Dietary supplement consumers

Industry/Entity Type

Dietary supplements

Font styles to use
Sans Serif

Colors

Designer to choose colors to be used in the design.

Requirements
Must have
• Trademark icon "®" has to be at the top right after the company logo(text of logo)/name.

```html
<!DOCTYPE html>
<html lang="en">
<head>
<meta charset="utf-8">
<title>Magnesium + B6 Label</title>
<link href="https://fonts.googleapis.com/css2?family=League+Gothic&family=Arimo:wght@700&display=swap" rel="stylesheet">
<style>
  :root {
    --backdrop: #eefcec;
    --label-white: #ffffff;
    --brand-green: #237d62;
    --title-ink: #2d2d2d;
    --band-violet: #c56af0;
    --band-lilac: #8a78f5;
    --band-blue: #4f7ef5;
    --badge-navy: #1b2a8c;
    --badge-ring: #1f4a3e;
    --art-pink: #e58ae8;
    --art-blue: #7f9cf2;
  }
  html, body {
    margin: 0;
    padding: 0;
    width: 1200px;
    height: 800px;
    overflow: hidden;
    background: var(--backdrop);
  }
  .label {
    position: absolute;
    left: 280px;
    top: 40px;
    width: 641px;
    height: 720px;
    background: var(--label-white);
    overflow: hidden;
  }
  .vector-art {
    position: absolute;
    left: 440px;
    top: 0;
    width: 201px;
    height: 222px;
    background: radial-gradient(ellipse 95% 90% at 85% 20%,
      var(--art-pink) 0%, var(--art-blue) 45%, rgba(127,156,242,.35) 75%, rgba(255,255,255,0) 100%);
  }
  .brand-name {
    position: absolute;
    left: 220px;
    width: 200px;
    top: 186px;
    margin: 0;
    text-align: center;
    font-family: "League Gothic", sans-serif;
    font-size: 46px;
    letter-spacing: 2px;
    line-height: 1;
    color: var(--brand-green);
  }
  .product-name {
    position: absolute;
    left: 0;
    width: 641px;
    top: 391px;
    margin: 0;
    text-align: center;
    font-family: "League Gothic", sans-serif;
    font-weight: 400;
    font-size: 88px;
    line-height: 1;
    color: var(--title-ink);
    transform: scaleX(0.8);
  }
  .product-band {
    position: absolute;
    left: 0;
    top: 555px;
    width: 641px;
    height: 69px;
    background: linear-gradient(90deg, var(--band-violet), var(--band-lilac) 55%, var(--band-blue));
  }
  .product-description {
    position: absolute;
    right: 174px;
    top: 0;
    margin: 0;
    line-height: 69px;
    font-family: "League Gothic", sans-serif;
    font-size: 36px;
    color: var(--label-white);
    white-space: nowrap;
    transform: scaleX(0.84);
    transform-origin: right center;
  }
  .intake-badge {
    position: absolute;
    left: 486px;
    top: 517px;
    width: 140px;
    height: 140px;
  }
  .intake-badge text {
    font-family: "Arimo", sans-serif;
    font-weight: 700;
  }
</style>
</head>
<body>
  <main class="label">
    <div class="vector-art" role="img" aria-label="Product vector art: cluster of pink and blue bubbles"></div>

    <p class="brand-name">VERDANT CALM</p>

    <h1 class="product-name">MAGNESIUM + B6</h1>

    <div class="product-band">
      <p class="product-description">MAGNESIUM WITH GINGER TASTE</p>
    </div>

    <svg class="intake-badge" viewBox="0 0 140 140" aria-label="Daily intake 1 capsule, 60 capsules">
      <defs>
        <radialGradient id="badge-fill" cx="50%" cy="40%" r="60%">
          <stop offset="0" stop-color="#f7c8f7"/>
          <stop offset="1" stop-color="#d85fe0"/>
        </radialGradient>
        <path id="badge-arc" d="M 16 92 A 56 56 0 1 1 124 92"/>
      </defs>
      <circle cx="70" cy="70" r="68" fill="var(--label-white)" stroke="var(--badge-ring)" stroke-width="2.5"/>
      <circle cx="70" cy="74" r="50" fill="url(#badge-fill)"/>
      <text font-size="11" fill="var(--badge-navy)" letter-spacing="0.8">
        <textPath href="#badge-arc" startOffset="50%" text-anchor="middle">DAILY INTAKE 1 CAPSULE</textPath>
      </text>
      <text x="70" y="80" text-anchor="middle" font-size="44" fill="var(--badge-navy)">60</text>
      <text x="70" y="98" text-anchor="middle" font-size="12" fill="var(--badge-navy)">Capsules</text>
    </svg>
  </main>
</body>
</html>
```